Modern Label for Loose Tea pouches on 4.5x6 Label

We need a new label for our teas that is very simple in design, but stylish and modern. This will be used to print labels for our loose tea pouches. The label will be at max 4.5x6 inches in size. There should be a place for the tea name, description, ingredients, and size that is changeable.
Preferably an AI file that allows me to setup variables to change the above items. There will also need to be our logo which is supplied, and our address on the label.
Address:
Brindle Teas
148 Lower Ferncliff Lane
Highland, NY 12097
Target Market(s)
Tea Lovers
Requirements
Must have
- Adobe Illustrator file with variables setup for replacement of tea name, description, ingredients, and size (weights 2oz, 4oz, 8oz, 1lb)

```html
<!DOCTYPE html>
<html lang="en">
<head>
<meta charset="utf-8">
<title>Brindle Teas – Acai Berry White Label</title>
<link href="https://fonts.googleapis.com/css2?family=Leckerli+One&family=Mulish:wght@400;700;800&family=Oswald:wght@600&family=Arimo:wght@700&display=swap" rel="stylesheet">
<style>
  :root {
    --leaf-green: #b9d532;
    --panel-green: #bad636;
    --ink: #111111;
    --shadow-ink: #3a3a3a;
    --chevron-shadow: #8a8a8e;
    --paper: #ffffff;
  }
  html, body {
    margin: 0;
    padding: 0;
    width: 900px;
    height: 1200px;
    overflow: hidden;
    background: var(--paper);
  }
  .label {
    position: relative;
    width: 900px;
    height: 1200px;
    font-family: "Mulish", sans-serif;
    color: var(--ink);
  }
  .brand-block {
    position: absolute;
    left: 207px;
    top: 0;
    width: 471px;
    height: 261px;
    background: var(--leaf-green);
  }
  .brand-mark {
    position: absolute;
    left: 50%;
    top: 78px;
    width: 52px;
    height: 52px;
    margin-left: -26px;
    border-radius: 50%;
    background: var(--paper);
  }
  .brand-name {
    position: absolute;
    left: 0;
    right: 0;
    top: 160px;
    text-align: center;
    font-family: "Mulish", sans-serif;
    font-weight: 800;
    font-size: 44px;
    letter-spacing: 2px;
    color: var(--paper);
  }
  .title-band {
    position: absolute;
    left: 67px;
    top: 270px;
    width: 758px;
    height: 122px;
    background: var(--leaf-green);
    border-radius: 12px;
    z-index: 2;
  }
  .tea-name {
    position: absolute;
    left: 0;
    right: 0;
    top: 10px;
    margin: 0;
    text-align: center;
    font-family: "Leckerli One", cursive;
    font-weight: 400;
    font-size: 76px;
    line-height: 1.2;
    color: var(--paper);
    text-shadow: 3px 4px 0 var(--shadow-ink);
  }
  .info-panel {
    position: absolute;
    left: 71px;
    top: 392px;
    width: 747px;
    height: 762px;
    background: var(--panel-green);
    border-radius: 0 0 26px 26px;
  }
  .chevron {
    position: absolute;
    left: 129px;
    top: 6px;
    width: 490px;
    height: 124px;
  }
  .description {
    position: absolute;
    left: 67px;
    top: 152px;
    width: 620px;
    margin: 0;
    font-size: 23.5px;
    line-height: 33.5px;
  }
  .ingredients {
    position: absolute;
    left: 93px;
    top: 350px;
    width: 580px;
    margin: 0;
    font-size: 23.5px;
    line-height: 33px;
  }
  .ingredients strong {
    font-weight: 800;
    font-size: 27px;
  }
  .net-weight {
    position: absolute;
    left: 0;
    right: 0;
    top: 520px;
    text-align: center;
    margin: 0;
    font-size: 30px;
  }
  .net-weight .net-label {
    font-family: "Oswald", sans-serif;
    font-weight: 600;
    letter-spacing: -1px;
  }
  .net-weight .net-value {
    font-family: "Arimo", sans-serif;
    font-weight: 700;
  }
  .address {
    position: absolute;
    left: 0;
    right: 0;
    top: 620px;
    margin: 0;
    text-align: center;
    font-size: 18.5px;
    padding-left: 28px;
  }
</style>
</head>
<body>
<div class="label">
  <header class="brand-block">
    <span class="brand-mark"></span>
    <div class="brand-name">Brindle Teas</div>
  </header>

  <div class="title-band">
    <h1 class="tea-name">Acai Berry White</h1>
  </div>

  <section class="info-panel">
    <svg class="chevron" viewBox="0 0 490 124" aria-hidden="true">
      <polygon points="0,52 245,124 490,52 490,60 245,124 0,60" fill="var(--chevron-shadow)"/>
      <polygon points="0,0 490,0 490,52 245,116 0,52" fill="var(--paper)"/>
      <polygon points="6,0 484,0 484,48 245,110 6,48" fill="var(--panel-green)"/>
    </svg>

    <p class="description">Delicious and good for you. This loose leaf white tea blend features “super food” acai mixed delicately with exotic, flavorful berries to create a deliciously flavorful white tea blend packed with antioxidants.</p>

    <p class="ingredients"><strong>INGREDIENTS</strong>: White tea scented with natural Acai berry and sprinkled with blue corn flowers.</p>

    <p class="net-weight"><span class="net-label">NET WT</span> <span class="net-value">1lb(454g)</span></p>

    <p class="address">ADDRESS: Brindle Teas | 148 Lower Ferncliff Lane | Highland, NY 12097</p>
  </section>
</div>
</body>
</html>
```